HVL Regal Business Card Design 2020

Harbor Vale Living is looking for a business card that is clean and straight to the point but still looks high-end and attractive. We are a team comprised of management and field professionals focused on the high-end residential marketplace. We serve homeowners and trade professionals directly based out of the Metrowest/Boston area. We provide client services as well as construction/renovation services.
We are aiming for a black and white feel (white background and black text) and a matte finish with rounded edges.

We want to emphasis our vision of "Properties - Projects - Partners".
Dana Pritchell is the president of HVL

Please include the following areas we service: Boston/Cape/Newport
Please make sure to include Dana's mobile (617) 555 0143 & office number (617) 555 0187, email dana@harborvaleliving.example and website www.harborvaleliving.example

Colors

Designer to choose only greyscale colors for use in the design.

Requirements
Must have
• Include "Properties - Projects - Partners" in design

Include "After Hours Emergency Support # 1800 555 0199" with icon

```html
<!DOCTYPE html>
<html lang="en">
<head>
<meta charset="utf-8">
<title>HVL Business Card – Front and Back</title>
<link rel="stylesheet" href="https://fonts.googleapis.com/css2?family=Montserrat:wght@600;700&family=Work+Sans:wght@400;500&display=swap">
<style>
  :root {
    --backdrop: #2a2a2a;
    --card-dark: #1c1c1c;
    --card-light: #ffffff;
    --ink: #1a1a1a;
    --ink-soft: #3a3a3a;
    --paper-text: #f2f2f2;
    --rule: #555555;
  }
  * { box-sizing: border-box; margin: 0; padding: 0; }
  html, body {
    width: 1200px; height: 930px; overflow: hidden;
    background: var(--backdrop);
  }
  .canvas { position: relative; width: 1200px; height: 930px; }
  .card {
    position: absolute; left: 250px; width: 700px; height: 400px;
    border-radius: 28px; overflow: hidden;
  }
  .card--back { top: 40px; background: var(--card-dark); color: var(--paper-text); }
  .card--front { top: 490px; background: var(--card-light); color: var(--ink); }

  .brand { font-family: "Montserrat", sans-serif; font-weight: 700; text-transform: uppercase; }
  .brand__mark { font-size: 84px; line-height: 1; letter-spacing: 2px; }
  .brand__name { font-size: 18px; letter-spacing: 2.5px; margin-top: 6px; }

  /* back */
  .card--back .brand { position: absolute; left: 0; right: 0; top: 70px; text-align: center; }
  .service { position: absolute; left: 0; right: 0; top: 228px; text-align: center; }
  .service__label { font-family: "Montserrat", sans-serif; font-weight: 600; font-size: 20px; letter-spacing: 1.5px; }
  .service__areas {
    position: absolute; left: 0; right: 0; top: 318px; text-align: center;
    font-family: "Work Sans", sans-serif; font-size: 19px; letter-spacing: 1.2px; text-transform: uppercase;
  }

  /* front */
  .card--front .brand { position: absolute; right: 70px; top: 42px; text-align: right; }
  .card--front .brand__mark { font-size: 70px; }
  .card--front .brand__name { font-size: 16px; }
  .rule { position: absolute; height: 1.5px; background: var(--rule); }
  .rule--top { left: 300px; right: 70px; top: 150px; }
  .rule--mid { left: 50px; width: 300px; top: 262px; }

  .person { position: absolute; left: 50px; top: 196px; }
  .person__name { font-family: "Montserrat", sans-serif; font-weight: 700; font-size: 28px; letter-spacing: 1px; text-transform: uppercase; }
  .person__title { font-family: "Work Sans", sans-serif; font-size: 17px; color: var(--ink-soft); margin-top: 2px; }

  .contact { position: absolute; left: 50px; top: 282px; list-style: none;
    font-family: "Work Sans", sans-serif; font-size: 17px; color: var(--ink-soft); }
  .contact li { display: flex; align-items: center; gap: 10px; height: 24px; }
  .contact svg, .emergency svg { width: 14px; height: 14px; fill: none; stroke: var(--ink); stroke-width: 1.6; flex: none; }

  .vision { position: absolute; right: 50px; top: 180px; text-align: right; list-style: none;
    font-family: "Montserrat", sans-serif; font-weight: 600; font-size: 23px; line-height: 1.2; text-transform: uppercase; }

  .emergency { position: absolute; right: 50px; top: 326px; display: flex; align-items: flex-start; gap: 10px;
    font-family: "Work Sans", sans-serif; font-size: 15px; line-height: 22px; color: var(--ink-soft); text-align: right; }
  .emergency svg { width: 18px; height: 18px; margin-top: 3px; }
  .emergency__number { font-weight: 500; color: var(--ink); }
</style>
</head>
<body>
<main class="canvas">
  <section class="card card--back" aria-label="Card back">
    <div class="brand">
      <div class="brand__mark">HVL</div>
      <div class="brand__name">Harbor Vale Living</div>
    </div>
    <div class="service"><p class="service__label">WE SERVICE</p></div>
    <p class="service__areas">Boston | Metrowest | South Shore | Cape/Newport</p>
  </section>

  <section class="card card--front" aria-label="Card front">
    <div class="brand">
      <div class="brand__mark">HVL</div>
      <div class="brand__name">Harbor Vale Living</div>
    </div>
    <div class="rule rule--top"></div>

    <div class="person">
      <p class="person__name">Dana Pritchell</p>
      <p class="person__title">President</p>
    </div>
    <div class="rule rule--mid"></div>

    <ul class="contact">
      <li><svg viewBox="0 0 16 16"><path d="M4 1.5l2.5 3-1.5 1.5c.8 2 2.5 3.7 4.5 4.5l1.5-1.5 3 2.5-1.5 2.5C6.5 14 2 9.5 1.5 3z"/></svg>(617) 555 0143</li>
      <li><svg viewBox="0 0 16 16"><rect x="4" y="1.5" width="8" height="13" rx="1.5"/><line x1="7" y1="12" x2="9" y2="12"/></svg>(617) 555 0187</li>
      <li><svg viewBox="0 0 16 16"><rect x="1.5" y="3.5" width="13" height="9" rx="1"/><path d="M1.5 4l6.5 5 6.5-5"/></svg>dana@harborvaleliving.example</li>
      <li><svg viewBox="0 0 16 16"><circle cx="8" cy="8" r="6.5"/><ellipse cx="8" cy="8" rx="3" ry="6.5"/><line x1="1.5" y1="8" x2="14.5" y2="8"/></svg>www.harborvaleliving.example</li>
    </ul>

    <ul class="vision">
      <li>Properties</li>
      <li>Projects</li>
      <li>Partners</li>
    </ul>

    <div class="emergency">
      <svg viewBox="0 0 16 16"><circle cx="8" cy="8" r="6.5"/><path d="M8 4v4.5l3 2"/></svg>
      <p>After Hours Emergency Support<br><span class="emergency__number"># 1800 555 0199</span></p>
    </div>
  </section>
</main>
</body>
</html>
```